Business Card Design needed for logo design project

Professional English School and translation company needs a business card design.

Target Market(s)

Wealthy business men. My company is called Meridian Tongue Partners.

Requirements
Must have
• I would like it to be a dark color with my logo.

```html
<!DOCTYPE html>
<html lang="en">
<head>
<meta charset="utf-8">
<title>Meridian Tongue Partners – Business Card</title>
<link href="https://fonts.googleapis.com/css2?family=Arimo:wght@400;700&display=swap" rel="stylesheet">
<style>
  :root {
    --page-bg: #2a2a2e;
    --card-dark-1: #55515f;
    --card-dark-2: #3f3c48;
    --card-light: #ffffff;
    --accent: #f39200;
    --text-light: #f2f1f5;
    --text-muted: #d9d7e0;
    --text-dark: #1d1c21;
    --rule: #8a8696;
  }
  * { box-sizing: border-box; margin: 0; padding: 0; }
  html, body { width: 1200px; height: 900px; overflow: hidden; }
  body {
    background: var(--page-bg);
    font-family: "Arimo", Arial, sans-serif;
    position: relative;
  }
  .card {
    position: absolute;
    top: 295px;
    width: 540px;
    height: 310px;
    border-radius: 22px;
    overflow: hidden;
    box-shadow: 0 10px 30px rgba(0,0,0,.45);
  }
  .card-front {
    left: 40px;
    background: radial-gradient(circle at 75% 30%, var(--card-dark-1), var(--card-dark-2) 75%);
  }
  .card-back { left: 620px; background: var(--card-dark-2); }

  .brand {
    display: flex;
    align-items: center;
    gap: 14px;
  }
  .brand-dot {
    width: 48px; height: 48px;
    border-radius: 50%;
    background: var(--accent);
    flex: none;
  }
  .brand-name {
    font-weight: 700;
    font-size: 30px;
    line-height: 1.05;
    letter-spacing: -0.2px;
  }
  .card-front .brand {
    position: absolute;
    left: 60px; top: 122px;
  }
  .card-front .brand-name { color: var(--text-light); }

  .back-top {
    position: absolute;
    left: 0; top: 0; right: 0;
    height: 152px;
    background: var(--card-light);
    border-bottom: 7px solid var(--accent);
  }
  .back-top .brand {
    position: absolute;
    left: 36px; top: 52px;
  }
  .back-top .brand-name { color: var(--text-dark); font-size: 27px; }
  .back-top .brand-dot { width: 44px; height: 44px; }

  .back-bottom {
    position: absolute;
    left: 0; right: 0; top: 152px; bottom: 0;
    background: radial-gradient(circle at 70% 10%, var(--card-dark-1), var(--card-dark-2) 80%);
    padding: 22px 36px;
    display: flex;
    gap: 28px;
  }
  .person { flex: 1; }
  .person-name {
    color: var(--accent);
    font-weight: 700;
    font-size: 22px;
    letter-spacing: 0.3px;
    margin-bottom: 16px;
    text-transform: uppercase;
  }
  .contact-list { list-style: none; }
  .contact-list li {
    display: flex;
    align-items: center;
    gap: 8px;
    color: var(--text-light);
    font-size: 13px;
    margin-bottom: 7px;
  }
  .contact-list svg { width: 13px; height: 13px; flex: none; }
  .address {
    width: 200px;
    border-left: 1px solid var(--rule);
    padding-left: 12px;
    align-self: flex-start;
    margin-top: 4px;
    color: var(--text-muted);
    font-size: 11.5px;
    line-height: 1.55;
    font-style: normal;
  }
</style>
</head>
<body>
  <section class="card card-front" aria-label="Business card front">
    <div class="brand">
      <span class="brand-dot"></span>
      <span class="brand-name">Meridian Tongue<br>Partners</span>
    </div>
  </section>

  <section class="card card-back" aria-label="Business card back">
    <div class="back-top">
      <div class="brand">
        <span class="brand-dot"></span>
        <span class="brand-name">Meridian Tongue<br>Partners</span>
      </div>
    </div>
    <div class="back-bottom">
      <div class="person">
        <h2 class="person-name">Daniel Varro</h2>
        <ul class="contact-list">
          <li>
            <svg viewBox="0 0 16 16" aria-hidden="true"><rect x="4" y="1" width="8" height="14" rx="1.5" fill="none" stroke="var(--accent)" stroke-width="1.6"/><circle cx="8" cy="12.3" r="0.9" fill="var(--accent)"/></svg>
            +47 900 12 345
          </li>
          <li>
            <svg viewBox="0 0 16 16" aria-hidden="true"><rect x="1" y="3" width="14" height="10" rx="1" fill="var(--accent)"/><path d="M1.5 3.5 8 9l6.5-5.5" fill="none" stroke="var(--card-dark-2)" stroke-width="1.3"/></svg>
            d.varro@meridiantongue.com
          </li>
          <li>
            <svg viewBox="0 0 16 16" aria-hidden="true"><circle cx="8" cy="8" r="6.5" fill="none" stroke="var(--accent)" stroke-width="1.5"/><path d="M1.5 8h13M8 1.5c-3 3.5-3 9.5 0 13M8 1.5c3 3.5 3 9.5 0 13" fill="none" stroke="var(--accent)" stroke-width="1.1"/></svg>
            www.meridiantonguepartners.com
          </li>
        </ul>
      </div>
      <address class="address">
        Meridian Tongue Partners<br>
        Rua das Palmeiras, 42 Sala 310<br>
        Porto Claro, RS, Brasil
      </address>
    </div>
  </section>
</body>
</html>
```